New Organic Skin Care Line Needs to Design a Product Label

***THE WINNER OF THIS PROJECT WILL MOST LIKELY BECOME THE EXCLUSIVE DESIGNER FOR OUR OTHER PRODUCT LABELS***

We need a label design for a new organic skin care product line called "Maple Dune Festoon." This specific product is a 100% pure organic coconut oil. It's used for skin hydration, protection, and makeup removal.

Info to include on front label:

1. Logo: Maple Dune Festoon (attached)
2. Product Name: Pure Coconut Oil (emphasize "organic" somewhere)
3. Slogan: Hydrate your skin and hair.
4. Size: 8 FL OZ 236mL

Attached is:

1. The brand logo "Maple Dune Festoon" with a white background.
2. An image of the bottle we will use.
3. An image of the bottle with lines to show the size and placement of the label.
4. The brand logo "Maple Dune Festoon" with a black background. (photoshop file)

What we need:

A simple mock up of the front side of the label on the bottle. We first want to know what it will look like on the bottle given the size and dimensions.

- We would like one label with a white background (including the logo with a white background).
- We would like a second label with a black background (including the logo with a black background, just need to make the black font white instead of black).

We can get a great idea of what to expect from the front side of the label so we will complete the back side once we identify a winner.
Updates

Apologies, but we are now using a different bottle. The previous one is now discontinued. Please view the two most recent images uploaded. One is an image of the new bottle by itself. The other is an image of that bottle with instructions. Please use your most recent designs on the new bottle. Feel free to make any modifications you see fit to compliment the new bottle shape. Added Friday, March 18, 2016

Project Deadline Extended
Reason: We are still working with the label company to finalize the size. Once the size is confirmed we will have to tweak labels based on finalized measurements.

Target Market(s)

Women, 18-70

Industry/Entity Type

Skin Care Product

Font styles to use
Decorative
Script

Requirements
Must have
• -"shabby sheek" and "cute" theme
• -soft organic feel
• -the ingredients are organic, pure, and natural. That should be an essence of the label.

```html
<!DOCTYPE html>
<html lang="en">
<head>
<meta charset="utf-8">
<title>Maple Dune Festoon — Pure Coconut Oil Label</title>
<link rel="stylesheet" href="https://fonts.googleapis.com/css2?family=Cinzel:wght@400;600&family=Cinzel+Decorative:wght@400&family=Roboto:wght@400&display=swap">
<style>
  :root {
    --canvas: #ffffff;
    --frame: #c9c9c9;
    --ink: #1d1d1d;
    --ribbon: #e89ac5;
    --ribbon-text: #ffffff;
    --tan: #c49a76;
    --pink: #e0388f;
    --visual-light: #c9a184;
    --visual-dark: #8a5a38;
  }
  * { margin: 0; padding: 0; box-sizing: border-box; }
  html, body {
    width: 1200px;
    height: 1000px;
    overflow: hidden;
    background: var(--canvas);
  }
  .canvas {
    position: relative;
    width: 1200px;
    height: 1000px;
  }
  .label {
    position: absolute;
    left: 350px;
    top: 130px;
    width: 500px;
    height: 740px;
    border: 2px solid var(--frame);
    background: var(--canvas);
  }
  .brand-name {
    position: absolute;
    left: 0;
    right: 0;
    top: 160px;
    text-align: center;
    font-family: "Cinzel", serif;
    font-weight: 400;
    font-size: 22px;
    letter-spacing: 4px;
    color: var(--ink);
  }
  .leaf-mark {
    position: absolute;
    left: 78px;
    top: 220px;
    width: 50px;
    height: 34px;
    border-radius: 17px;
    background: var(--ribbon);
  }
  .organic-ribbon {
    position: absolute;
    left: -4px;
    top: 256px;
    width: 232px;
    height: 88px;
  }
  .organic-ribbon svg { position: absolute; inset: 0; }
  .organic-ribbon .ribbon-text {
    position: absolute;
    left: 20px;
    top: 6px;
    font-family: "Cinzel", serif;
    font-size: 32px;
    line-height: 38px;
    letter-spacing: 1px;
    color: var(--ribbon-text);
  }
  .product-visual {
    position: absolute;
    left: 246px;
    top: 284px;
    width: 214px;
    height: 136px;
    border-radius: 18px;
    background: linear-gradient(135deg, var(--visual-light), var(--visual-dark));
  }
  .product-name {
    position: absolute;
    left: 0;
    top: 362px;
    width: 100%;
    font-family: "Cinzel", serif;
    color: var(--tan);
  }
  .product-name .line { position: absolute; white-space: nowrap; line-height: 1; }
  .product-name .pure { left: 26px; top: 0; font-size: 64px; font-weight: 400; letter-spacing: 2px; }
  .product-name .coconut { left: 34px; top: 66px; font-size: 76px; font-weight: 600; }
  .product-name .oil { left: 290px; top: 134px; font-size: 76px; font-weight: 600; }
  .tagline {
    position: absolute;
    left: 0;
    right: 0;
    top: 596px;
    text-align: center;
    font-family: "Cinzel Decorative", serif;
    font-size: 27px;
    color: var(--pink);
  }
  .volume {
    position: absolute;
    left: 0;
    right: 0;
    top: 688px;
    text-align: center;
    font-family: "Roboto", sans-serif;
    font-size: 16px;
    word-spacing: 2px;
    color: var(--ink);
  }
</style>
</head>
<body>
<main class="canvas">
  <section class="label">
    <div class="brand-name">Maple Dune Festoon</div>

    <div class="leaf-mark" role="img" aria-label="Small pink leaf sprig accent"></div>

    <div class="organic-ribbon">
      <svg width="232" height="88" viewBox="0 0 232 88">
        <polygon points="0,0 232,0 208,44 232,88 0,88" fill="var(--ribbon)"/>
      </svg>
      <div class="ribbon-text">100% PURE<br>ORGANIC</div>
    </div>

    <div class="product-visual" role="img" aria-label="Photo of a halved coconut with a pink orchid blossom"></div>

    <h1 class="product-name">
      <span class="line pure">PURE</span>
      <span class="line coconut">COCONUT</span>
      <span class="line oil">OIL</span>
    </h1>

    <p class="tagline">Hydrate your skin and hair</p>
    <p class="volume">8 FL OZ &nbsp;&nbsp; 236ML</p>
  </section>
</main>
</body>
</html>
```